48207 Velmont Lane Ad (for Facebook and Instagram)

Ad to run on Social Media (i.e. Facebook, Instagram etc.)
to advertise sale of property.

Target Market(s)

Prospective Buyers

Requirements
Must have
• TEXT
• Presenting
• 48207 Velmont Lane, Brandywine, MD
• Priced to Sell
• 5 Bedroom / 4 Bathroom Colonial with Contemporary Design and Charm
• Over 5,000 sq ft of Spacious Elegance
• Extraordinary Master Bedroom with Spacious Bath
• Modern Open Concept Kitchen
• Natural Oak Floors
• Stainless Steel Appliances
• Granite Counter-Tops
• Exterior with Outdoor Security, Design Lighting and Sprinkler System
• Just 10 Minutes From Corwen Quay
• Call Marcus Pendley, Realtor
• Tolbrook Realty Inc.
• Phone (240) 555-0187
• Email - premierhomedesk@mailbrook.test

```html
<!DOCTYPE html>
<html lang="en">
<head>
<meta charset="utf-8">
<title>48207 Velmont Lane – For Sale</title>
<link href="https://fonts.googleapis.com/css2?family=Montserrat:wght@800&family=Roboto:wght@400;500;700&display=swap" rel="stylesheet">
<style>
  :root {
    --stage: #e9e9e9;
    --navy: #0b2f86;
    --blue: #1a6cc4;
    --sky: #3d9ee2;
    --panel: #e9ecef;
    --ink: #222428;
    --white: #ffffff;
    --paper: #f7f9fb;
  }
  * { margin: 0; padding: 0; box-sizing: border-box; }
  html, body { width: 1200px; height: 435px; overflow: hidden; background: var(--stage); }
  body { font-family: "Roboto", Arial, sans-serif; color: var(--ink); position: relative; }

  .ad-frame { position: absolute; left: 0; top: 76px; width: 1200px; height: 283px; overflow: hidden; }
  .ad { position: absolute; left: 0; top: 0; width: 1377px; height: 324px; background: var(--paper);
        transform: scale(0.8715); transform-origin: 0 0; }
  .ad svg.backdrop { position: absolute; inset: 0; }

  .headline { position: absolute; left: 70px; top: 70px; width: 240px; text-align: center; color: var(--white); }
  .headline h1 { font-family: "Montserrat", Arial, sans-serif; font-weight: 800; font-size: 82px; line-height: 0.86; letter-spacing: 1px; }
  .headline .presenting { font-size: 10px; font-weight: 700; margin-top: 16px; }
  .headline .address { font-size: 13px; margin-top: 4px; white-space: nowrap; }

  .agent-photo { position: absolute; left: 812px; top: 169px; width: 164px; height: 155px; }

  .about { position: absolute; left: 322px; top: 60px; width: 548px; height: 202px; background: var(--panel);
           border-top: 5px solid var(--blue); }
  .about .tab { position: absolute; left: 0; top: -5px; height: 30px; width: 186px; background: var(--blue);
                clip-path: polygon(0 0, 100% 0, 93% 100%, 0 100%); color: var(--white);
                font-weight: 700; font-size: 16px; line-height: 30px; padding-left: 22px; }
  .about .features { position: absolute; top: 48px; left: 16px; right: 8px; display: flex; gap: 12px; }
  .about ul { list-style: none; flex: 1; }
  .about ul:first-child { flex: 0 0 250px; }
  .about li { font-size: 13.5px; line-height: 16px; padding-left: 16px; position: relative; margin-bottom: 11px; }
  .about li svg { position: absolute; left: 0; top: 3px; }

  .tag { position: absolute; background: var(--blue); color: var(--white); text-align: center; font-weight: 700; }
  .tag.price { left: 896px; top: 60px; width: 198px; height: 48px; clip-path: polygon(0 0, 88% 0, 100% 100%, 12% 100%); padding-top: 8px; }
  .tag.price small { display: block; font-size: 12px; font-weight: 500; }
  .tag.price strong { display: block; font-size: 19px; letter-spacing: 0.3px; }
  .tag.firm { left: 944px; top: 117px; width: 170px; height: 33px; clip-path: polygon(0 0, 90% 0, 100% 100%, 10% 100%); font-size: 15px; line-height: 33px; }
  .tag.mail { left: 907px; top: 158px; width: 232px; height: 31px; clip-path: polygon(0 0, 93% 0, 100% 100%, 4% 100%); font-size: 12px; font-weight: 400; line-height: 31px; }

  .agent { position: absolute; left: 936px; top: 200px; text-align: right; width: 194px; }
  .agent .name { color: var(--blue); font-size: 16px; }
  .agent .name small { color: var(--ink); font-size: 11px; font-weight: 700; }
  .agent .call { font-size: 17px; font-weight: 700; margin-top: 2px; }
  .agent .marks { display: flex; justify-content: flex-end; align-items: center; gap: 12px; margin-top: 10px; }
  .agent .brand { font-size: 13px; font-weight: 700; color: var(--navy); letter-spacing: 0.5px; }
  .agent .badge { width: 28px; height: 34px; background: var(--blue); }
</style>
</head>
<body>
<div class="ad-frame">
  <div class="ad">
    <svg class="backdrop" width="1377" height="324" viewBox="0 0 1377 324">
      <defs>
        <linearGradient id="blueField" x1="0" y1="1" x2="1" y2="0">
          <stop offset="0" stop-color="#0a2a82"/>
          <stop offset="0.55" stop-color="#1a63c3"/>
          <stop offset="1" stop-color="#45a6e6"/>
        </linearGradient>
        <linearGradient id="houseTone" x1="0" y1="0" x2="0" y2="1">
          <stop offset="0" stop-color="#e6ebf1"/>
          <stop offset="0.55" stop-color="#9a6a55"/>
          <stop offset="1" stop-color="#f1f3f6"/>
        </linearGradient>
        <linearGradient id="harborTone" x1="0" y1="0" x2="1" y2="1">
          <stop offset="0" stop-color="#5a4e9c"/>
          <stop offset="0.5" stop-color="#c04a8a"/>
          <stop offset="1" stop-color="#2b3f8c"/>
        </linearGradient>
      </defs>
      <polygon points="0,0 597,0 495,324 0,324" fill="url(#blueField)"/>
      <polygon role="img" aria-label="Photo of the colonial house in snow" points="1079,0 1289,0 1320,97 1240,133 1094,133 1064,32" fill="url(#houseTone)"/>
      <polygon role="img" aria-label="Photo of the waterfront with lit ferris wheel at night" points="1320,118 1377,112 1377,324 1229,324 1163,214" fill="url(#harborTone)"/>
    </svg>

    <svg class="agent-photo" viewBox="0 0 164 155" role="img" aria-label="Portrait of realtor Marcus Pendley in a dark suit">
      <polygon points="62,0 100,0 106,70 104,92 150,108 164,155 0,155 12,108 58,92 56,70" fill="#2c2c30"/>
    </svg>

    <div class="headline">
      <h1>FOR<br>SALE</h1>
      <p class="presenting">Presenting</p>
      <p class="address">48207 Velmont Lane, Brandywine, MD</p>
    </div>

    <section class="about">
      <div class="tab">ABOUT PROPERTY</div>
      <div class="features">
        <ul>
          <li><svg width="11" height="9" viewBox="0 0 11 9"><path d="M1 4.5 4 7.5 10 1" fill="none" stroke="#222" stroke-width="2"/></svg>5 Bedroom / 4 Bathroom Colonial with Contemporary Design and Charm</li>
          <li><svg width="11" height="9" viewBox="0 0 11 9"><path d="M1 4.5 4 7.5 10 1" fill="none" stroke="#222" stroke-width="2"/></svg>Over 5,000 sq ft of Spacious Elegance</li>
          <li><svg width="11" height="9" viewBox="0 0 11 9"><path d="M1 4.5 4 7.5 10 1" fill="none" stroke="#222" stroke-width="2"/></svg>Modern Open Concept Kitchen</li>
          <li><svg width="11" height="9" viewBox="0 0 11 9"><path d="M1 4.5 4 7.5 10 1" fill="none" stroke="#222" stroke-width="2"/></svg>Natural Oak Floors</li>
          <li><svg width="11" height="9" viewBox="0 0 11 9"><path d="M1 4.5 4 7.5 10 1" fill="none" stroke="#222" stroke-width="2"/></svg>Stainless Steel Appliances</li>
        </ul>
        <ul>
          <li><svg width="11" height="9" viewBox="0 0 11 9"><path d="M1 4.5 4 7.5 10 1" fill="none" stroke="#222" stroke-width="2"/></svg>Extraordinary Master Bedroom with Spacious Bath</li>
          <li><svg width="11" height="9" viewBox="0 0 11 9"><path d="M1 4.5 4 7.5 10 1" fill="none" stroke="#222" stroke-width="2"/></svg>Granite Counter-Tops</li>
          <li><svg width="11" height="9" viewBox="0 0 11 9"><path d="M1 4.5 4 7.5 10 1" fill="none" stroke="#222" stroke-width="2"/></svg>Exterior with Outdoor Security, Design Lighting and Sprinkler System</li>
          <li><svg width="11" height="9" viewBox="0 0 11 9"><path d="M1 4.5 4 7.5 10 1" fill="none" stroke="#222" stroke-width="2"/></svg>Just 10 Minutes From Corwen Quay</li>
        </ul>
      </div>
    </section>

    <div class="tag price"><small>Priced to Sell</small><strong>Only $550,000</strong></div>
    <div class="tag firm">Tolbrook Realty Inc.</div>
    <div class="tag mail">premierhomedesk@mailbrook.test</div>

    <div class="agent">
      <p class="name">Marcus Pendley, <small>Realtor</small></p>
      <p class="call">Call: (240) 555-0187</p>
      <div class="marks">
        <span class="brand">TOLBROOK</span>
        <span class="badge"></span>
      </div>
    </div>
  </div>
</div>
</body>
</html>
```